Tovrel Business Card

We are a modern retail clothing store. Established in 1994. I need a presentable card that will amaze vendors when given to them.

Front: Logo in middle
Info Side:

Name: Omar Latif
Cell: 630-555-0148
Work: 630-555-0192 EXT. 230
Email: Omar@tovrel.example
Website: www.Tovrel.example

Industry/Entity Type

Business

```html
<!DOCTYPE html>
<html lang="en">
<head>
<meta charset="utf-8">
<title>Tovrel Business Card</title>
<link rel="stylesheet" href="https://fonts.googleapis.com/css2?family=Open+Sans:wght@400;600&display=swap">
<style>
  :root {
    --page-bg: #e9e7e3;
    --silver-light: #d9d9d9;
    --silver-mid: #a9a9a9;
    --silver-dark: #8a8a8a;
    --ink-dark: #1a1a1a;
    --card-black: #0c0c0c;
    --card-black-soft: #2a2a2a;
    --text-light: #e6e6e6;
    --text-muted: #bdbdbd;
    --divider: #6a6a6a;
  }
  * { box-sizing: border-box; margin: 0; padding: 0; }
  html, body {
    width: 1200px; height: 871px; overflow: hidden;
    background: var(--page-bg);
    font-family: "Open Sans", Arial, sans-serif;
  }
  .canvas {
    width: 1200px; height: 871px;
    display: flex; flex-direction: column;
    align-items: center; justify-content: center; gap: 56px;
  }
  .card {
    width: 560px; height: 320px;
    border-radius: 22px;
    position: relative;
    box-shadow: 0 10px 26px rgba(0,0,0,0.22);
    overflow: hidden;
  }
  .card--front {
    background: linear-gradient(120deg, var(--silver-mid) 0%, var(--silver-light) 45%, var(--silver-dark) 100%);
    display: flex; align-items: center; justify-content: center;
  }
  .brand-name {
    font-weight: 600;
    font-size: 64px;
    letter-spacing: 3px;
    text-transform: uppercase;
    line-height: 1;
  }
  .card--front .brand-name { color: var(--ink-dark); }
  .card--info {
    background: linear-gradient(125deg, var(--card-black-soft) 0%, var(--card-black) 40%, var(--card-black) 100%);
  }
  .card--info .brand-name {
    position: absolute; left: 40px; top: 128px;
    color: var(--text-light);
    font-size: 52px;
  }
  .divider {
    position: absolute; left: 315px; top: 62px;
    width: 1px; height: 196px;
    background: linear-gradient(to bottom, transparent, var(--divider) 25%, var(--divider) 75%, transparent);
  }
  .contact {
    position: absolute; left: 340px; top: 74px;
    color: var(--text-light);
  }
  .contact__name { font-size: 19px; font-weight: 600; color: var(--text-muted); }
  .contact__title { font-size: 15px; margin-bottom: 20px; }
  .contact__list { list-style: none; }
  .contact__item {
    display: flex; align-items: center; gap: 9px;
    font-size: 14.5px; line-height: 23px;
  }
  .contact__icon { width: 13px; height: 13px; flex: none; fill: var(--text-muted); }
</style>
</head>
<body>
<main class="canvas">
  <section class="card card--front" aria-label="Card front">
    <span class="brand-name">Tovrel</span>
  </section>

  <section class="card card--info" aria-label="Card info side">
    <span class="brand-name">Tovrel</span>
    <div class="divider"></div>
    <div class="contact">
      <p class="contact__name">Omar Latif</p>
      <p class="contact__title">CEO/Founder</p>
      <ul class="contact__list">
        <li class="contact__item">
          <svg class="contact__icon" viewBox="0 0 16 16" aria-hidden="true"><path d="M4 0h8a1 1 0 0 1 1 1v14a1 1 0 0 1-1 1H4a1 1 0 0 1-1-1V1a1 1 0 0 1 1-1zm1 2v10h6V2zm3 11a1 1 0 1 0 0 2 1 1 0 0 0 0-2z"/></svg>
          630-555-0148
        </li>
        <li class="contact__item">
          <svg class="contact__icon" viewBox="0 0 16 16" aria-hidden="true"><path d="M3.6 0.6l2.3 2.9c.3.4.3 1-.1 1.4L4.6 6.1c.9 2 2.6 3.8 4.7 4.8l1.2-1.2c.4-.4 1-.4 1.4-.1l2.9 2.3c.4.3.5 1 .1 1.4l-1.5 1.5C11.9 16.3 0 8 .6 2.2L2.2.5c.4-.4 1.1-.3 1.4.1z"/></svg>
          630-555-0192 EXT. 230
        </li>
        <li class="contact__item">
          <svg class="contact__icon" viewBox="0 0 16 16" aria-hidden="true"><path d="M0 3h16v10H0zM1.5 4.2v.5L8 9l6.5-4.3v-.5z"/></svg>
          Omar@tovrel.example
        </li>
        <li class="contact__item">
          <svg class="contact__icon" viewBox="0 0 16 16" aria-hidden="true"><path d="M8 0a8 8 0 1 0 0 16A8 8 0 0 0 8 0zm0 1.6c.8 0 1.8 1.9 2 5.6H6c.2-3.7 1.2-5.6 2-5.6zM4.4 7.2H1.7a6.4 6.4 0 0 1 3.6-5c-.5 1.2-.8 3-.9 5zm0 1.6c.1 2 .4 3.8.9 5a6.4 6.4 0 0 1-3.6-5zM6 8.8h4c-.2 3.7-1.2 5.6-2 5.6s-1.8-1.9-2-5.6zm5.6 0h2.7a6.4 6.4 0 0 1-3.6 5c.5-1.2.8-3 .9-5zm0-1.6c-.1-2-.4-3.8-.9-5a6.4 6.4 0 0 1 3.6 5z"/></svg>
          www.Tovrel.example
        </li>
      </ul>
    </div>
  </section>
</main>
</body>
</html>
```